Marwick Estate Services (Handyman / Home Improvement Company)

Looking for a double sided professional looking business card with Logo attached to be highlighted on one side and throwing in an image of a handyman as an option would be nice to see as well. We are a company focused on providing quality Handyman and Home improvement services in a timely manner that is done right the first time with integrity

Industry/Entity Type

Handyman / Home Improvement

Contact Information for Business Card

(LOGO, Name, Mobile and office phone numbers, email) on front side of card, (the words "The SOLUTION to all of your Handyman and Home Improvement needs" followed by "Family Owned and Operated" at the very bottom) on the back.

Colors
EB3D1F
EC4F4E
F09395
F8D3D4
FCEDEE

Requirements
Must have
• Red, Gray, Black Color scheme
Should not have
• No Yellow or Blue colors

```html
<!DOCTYPE html>
<html lang="en">
<head>
<meta charset="utf-8">
<title>Marwick Estate Services – Business Card</title>
<link rel="stylesheet" href="https://fonts.googleapis.com/css2?family=Anton&family=Montserrat:wght@400;500;600;700&display=swap">
<style>
  :root {
    --red: #e8262b;
    --red-deep: #eb3d1f;
    --ink: #1b1b1b;
    --charcoal: #333333;
    --band-dark: #3a3a3a;
    --stage: #1c1c1c;
    --card-top: #a3a3a3;
    --card-mid: #ffffff;
    --card-bottom: #b9b9b9;
    --art-tone: #c9c9cc;
  }
  * { box-sizing: border-box; margin: 0; padding: 0; }
  html, body { width: 1200px; height: 1059px; overflow: hidden; }
  body {
    background: var(--stage);
    font-family: "Montserrat", Arial, sans-serif;
    position: relative;
  }
  .card {
    position: absolute;
    left: 262px;
    width: 715px;
    height: 410px;
    border-radius: 24px;
    overflow: hidden;
    background: linear-gradient(180deg, var(--card-top) 0%, #e4e4e4 35%, var(--card-mid) 50%, #e6e6e6 68%, var(--card-bottom) 100%);
  }
  .card--front { top: 94px; }
  .card--back { top: 529px; }

  /* front */
  .brand-name {
    position: absolute;
    left: 0; right: 0; top: 170px;
    text-align: center;
    font-weight: 700;
    font-size: 38px;
    letter-spacing: 0.5px;
    color: var(--ink);
  }
  .person {
    position: absolute;
    right: 386px; top: 283px;
    text-align: right;
  }
  .person__name {
    font-weight: 700;
    font-size: 28px;
    color: var(--red);
    line-height: 1.1;
  }
  .person__role {
    font-size: 20px;
    color: var(--ink);
    margin-top: 6px;
  }
  .divider {
    position: absolute;
    left: 357px; top: 268px;
    width: 2px; height: 94px;
    background: linear-gradient(180deg, transparent, var(--red) 20%, var(--red) 80%, transparent);
  }
  .contacts {
    position: absolute;
    left: 380px; top: 268px;
    list-style: none;
  }
  .contacts li {
    display: flex;
    align-items: center;
    height: 31px;
    font-size: 19px;
    color: var(--ink);
  }
  .contacts svg { width: 18px; height: 18px; margin-right: 14px; fill: var(--red); flex: none; }
  .band {
    position: absolute;
    left: 0; right: 0; bottom: 0;
    height: 12px;
    background: linear-gradient(100deg, var(--red) 0 49.6%, #9a9a9a 49.6% 50.4%, var(--band-dark) 50.4% 100%);
  }

  /* back */
  .tagline {
    position: absolute;
    left: 25px; top: 50px;
    width: 400px;
    text-align: center;
  }
  .tagline__lead {
    font-weight: 700;
    font-size: 28px;
    color: var(--charcoal);
    line-height: 38px;
  }
  .tagline__main {
    font-family: "Anton", Impact, sans-serif;
    font-size: 43px;
    line-height: 56px;
    color: var(--red);
    letter-spacing: -0.5px;
    margin-top: 2px;
  }
  .family {
    position: absolute;
    left: 40px; top: 357px;
    font-weight: 700;
    font-size: 22px;
    color: var(--charcoal);
  }
  .handyman-art {
    position: absolute;
    left: 438px; top: 18px;
    width: 268px; height: 380px;
    border-radius: 12px;
    background: linear-gradient(180deg, #d8d8da 0%, var(--art-tone) 60%, #b3b3b6 100%);
  }
</style>
</head>
<body>
  <section class="card card--front">
    <div class="brand-name">Marwick Estate Services</div>

    <div class="person">
      <div class="person__name">Daniel Harper</div>
      <div class="person__role">Owner</div>
    </div>
    <div class="divider"></div>
    <ul class="contacts">
      <li>
        <svg viewBox="0 0 24 24" aria-hidden="true"><path d="M7 1h10a2 2 0 0 1 2 2v18a2 2 0 0 1-2 2H7a2 2 0 0 1-2-2V3a2 2 0 0 1 2-2zm0 3v14h10V4H7zm5 15.5a1.2 1.2 0 1 0 0 2.4 1.2 1.2 0 0 0 0-2.4z"/></svg>
        055-718 204 963
      </li>
      <li>
        <svg viewBox="0 0 24 24" aria-hidden="true"><path d="M2 8c0-3 4-5 10-5s10 2 10 5v2h-5V8H7v2H2V8zm4 4h12l3 9H3l3-9zm6 2a3 3 0 1 0 0 6 3 3 0 0 0 0-6z"/></svg>
        055-718 204 970
      </li>
      <li>
        <svg viewBox="0 0 24 24" aria-hidden="true"><path d="M2 5h20v14H2V5zm2 2v.5l8 5.5 8-5.5V7H4zm0 3v7h16v-7l-8 5.5L4 10z"/></svg>
        hello@marwickestate.com
      </li>
    </ul>
    <div class="band"></div>
  </section>

  <section class="card card--back">
    <div class="tagline">
      <p class="tagline__lead">Your SOLUTION to all of</p>
      <p class="tagline__main">your Handyman and<br>Home Improvement<br>Needs</p>
    </div>
    <p class="family">Family Owned and Operated</p>
    <div class="handyman-art" role="img" aria-label="Cartoon handyman in work overalls holding a pipe wrench and a spanner"></div>
  </section>
</body>
</html>
```